KeyHarbor needs a modern business card

We are a modern conveyancing company and we need to appeal to the top (Multi-million dollar properties)and bottom on the property conveyancing market but our sweet spot is the middle of the market. I like professional with a hint of unconventional.

Target Market(s)

As above

Industry/Entity Type

Real Estate

Contact Information for Business Card

Back Of card:
thinking black with the logo and a tag line (I could be wrong about the black)
Tag line - Clear Advice, Careful Settlement

Front of Card:
Marissa Toll (BBus (Finance) LLB)
Licensed Conveyancer
Email: marissa@keyharbor.com.au

Key Harbor
ABN: 48 913 706
Suite 14, Level 3, 9 Calloway Road Lindhurst Park, NSW 2178
Phone: 1300 682 917

Sydney - Melbourne - Brisbane (Perhaps have this along the bottom of the card)

Requirements
Must have
• Sleek, modern and top end appeal (But approachable)
Should not have
• Not too cluttered

```html
<!DOCTYPE html>
<html lang="en">
<head>
<meta charset="utf-8">
<title>Key Harbor — Business Card</title>
<link href="https://fonts.googleapis.com/css2?family=Arimo:wght@400;700&display=swap" rel="stylesheet">
<style>
  :root {
    --backdrop: #b9b9b9;
    --card-white: #f7f7f7;
    --card-black: #141516;
    --navy: #2f5778;
    --navy-deep: #1f4566;
    --sky: #3aaedb;
    --lime: #9fcd4a;
    --green: #6cbf52;
    --text-grey: #555a5e;
    --rule: #8a8a8a;
    --white: #ffffff;
  }
  * { box-sizing: border-box; margin: 0; padding: 0; }
  html, body {
    width: 1200px;
    height: 900px;
    overflow: hidden;
    background: var(--backdrop);
    font-family: "Arimo", Arial, sans-serif;
  }
  .canvas {
    position: relative;
    width: 1200px;
    height: 900px;
  }
  .card {
    position: absolute;
    width: 560px;
    height: 340px;
    border-radius: 18px;
    overflow: hidden;
  }
  .card--front {
    left: 120px;
    top: 80px;
    background: linear-gradient(90deg, var(--white), var(--card-white) 60%, #e4e4e4);
  }
  .card--back {
    left: 520px;
    top: 480px;
    background: linear-gradient(90deg, #222426, var(--card-black) 70%, #050505);
  }

  /* front side */
  .front-accent {
    position: absolute;
    top: 0;
    width: 150px;
    height: 100%;
  }
  .front-accent--left {
    left: 0;
    background: linear-gradient(180deg, var(--navy) 0%, var(--navy) 45%, var(--green) 60%, var(--lime) 100%);
  }
  .front-accent--right {
    right: 0;
    background: linear-gradient(180deg, var(--navy-deep) 0%, var(--navy-deep) 40%, #3f78b6 55%, var(--sky) 100%);
  }
  .front-details {
    position: absolute;
    left: 150px;
    right: 150px;
    top: 30px;
    text-align: center;
    color: var(--text-grey);
    font-size: 14.5px;
    line-height: 1.22;
  }
  .holder-name {
    color: var(--navy);
    font-weight: 700;
    font-size: 24px;
    letter-spacing: 0.5px;
    margin-bottom: 3px;
  }
  .label { font-weight: 700; }
  .divider {
    border: none;
    border-top: 1.5px dashed var(--rule);
    margin: 10px 0;
  }
  .company-name {
    color: var(--navy);
    font-weight: 700;
    font-size: 15px;
  }
  .offices {
    font-size: 14.5px;
    letter-spacing: 0.4px;
  }

  /* back side */
  .back-content {
    position: absolute;
    inset: 0;
    display: flex;
    flex-direction: column;
    align-items: center;
    justify-content: center;
    color: var(--white);
  }
  .brand-mark {
    width: 22px;
    height: 22px;
    background: var(--sky);
    margin-bottom: 18px;
  }
  .brand-name {
    font-size: 40px;
    font-weight: 700;
    letter-spacing: -0.5px;
  }
  .tagline {
    margin-top: 12px;
    font-size: 16px;
    letter-spacing: 0.6px;
  }
</style>
</head>
<body>
<main class="canvas">
  <section class="card card--front">
    <div class="front-accent front-accent--left" role="img" aria-label="Geometric blue and green folded-band decoration"></div>
    <div class="front-accent front-accent--right" role="img" aria-label="Geometric navy and cyan folded-band decoration"></div>
    <div class="front-details">
      <p class="holder-name">Marissa Toll</p>
      <p>(BBus (Finance) LLB)</p>
      <p>Licensed Conveyancer</p>
      <p><span class="label">E.</span> marissa@keyharbor.com.au</p>
      <hr class="divider">
      <p class="company-name">Key Harbor</p>
      <p>ABN: 48 913 706</p>
      <p>Suite 14, Level 3,</p>
      <p>9 Calloway Road Lindhurst Park,</p>
      <p>NSW 2178</p>
      <p><span class="label">P.</span> 1300 682 917</p>
      <hr class="divider">
      <p class="offices">Sydney - Melbourne - Brisbane</p>
    </div>
  </section>

  <section class="card card--back">
    <div class="back-content">
      <span class="brand-mark"></span>
      <p class="brand-name">KeyHarbor</p>
      <p class="tagline">Clear Advice, Careful Settlement</p>
    </div>
  </section>
</main>
</body>
</html>
```